Norwegian psychologist service needs a fresh and exiting web site*

Norwegian psychologist service: working with therapy, personal development, mastery and personal growth. Focus: children and teenagers with special needs; family dynamics; group processes; individuals with a need for therapy and personal growth. (Our company name: Fjordlys og samhold (means Mastery and Growth).

We already have a logo for the company, which will be used (will be attached in the project).

The webside is to be structured in 4 pages with roll down curtain menus (the numbers are just for guiding the designer - the should not be added):

Page 1: Om Fjordlys og Samhold (about Mastery and Growth): this is where our business is is presented/described shortly: Lorem Ipsum dolor cit...

Page 2: Tjenester (Services): this is where our 5 service areas are presented:
2.1 Utredning (Investigation, diagnosing): Lorem Ipsum dolor cit...
2.2 Rådgivning (consulting): Lorem Ipsum dolor cit...

2.3 Kurs og work shops (courses and work shops): Lorem Ipsum dolor cit...
2.3a Fjordlys og samhold Tema 1 (T1)
2.3b Fjordlys og samhold Tema 2 (T2)
2.3c Fjordlys og samhold Tema 3 (T3)

2.4 Terapi og utvikling (Therapy and development)
2.4a Fjordlys og samhold for individer (FS1)
2.4b Fjordlys og samhold i familier (FS2)
2.4c Fjordlys og samhold i grupper (FS3)
2.4d Fjordlys og samhold i institusjoner (FS4)

Page 3: Aktuelt (Blog): this is our blog where we share knowledge and articles

Page 4: Kontakt (Contact): This is the contact form page. Contact form should constitute:
- Ditt navn (your name)
- E-post (your e-mail)
- Emne (subject)
- Melding (message/description)

Our project should also include suggestion for handheld units (iPhone, iPad).
Updates

We have both been traveling with work for a while, and then unfortunately both of us got sick on return, so we need a few more days to evaluate and choose design. Kind Regards Arvid & Margit

Target Market(s)

Focus on therapy, learning, mastery and growth for children and teenagers with special needs, within the family dynamics, or in a group setting.
OUR MARKETS:
Private market: individuals, families, groups and health industry institutions (with focus on learning, mastery, growth (as well as growing up) and psychiatry for children and teenagers with special difficulties and needs)
Public institutions: Government institutions, state institutions and municipality institutions (e.g. schools, municipality health service, hospitals) that serve the public (families with children and teenagers with special needs, and where learning, mastery, growth (as well as growing up) and potential psychiatry is an issue).

Number of Pages Required

4 page

Font styles to use
Sans Serif

Colors

Designer to choose colors to be used in the design.

Requirements
Must have
• The website must have 4 pages with roll down curtain menus (we have added a PDF with suggested structure, and headings, with sub menus - see attached PDF drawing.
• The web page must also use the added logo file - and make the web page work well with our logo.
• We would like the website to have a modern look and we would like the site to be associated with typical HIGH END TOP QUALITY private health institutions, but with a stronger focus on human beings (hands, faces etc), and not white coats and doctors. We are psychologists in the private market.
• For instance, if photos are being used - we tend to like "warm" almost art-like, "grainy" two-tone (e.g. sepia) photos to illustrate our focus. If designer can find such photos as part of design, it would be interesting to us. We would like a few photos like that integrated in the design.
• We also want a design suggestion for how the web page should look like and behave on handheld units (e.g. iPhone, iPad).
Nice to have
• If designer could find a number of suitable photos that matches the business idea and design requirements (see description above), that could follow website, that would be good.
• It could also be nice to have graphic symbols that denote the different pages/subpages (subjects)....
• HORSES: we sometimes use horses as a "tool" in therapy sessions. The horse is not necessarily used for riding, but for contact, communication and grooming. PHOTOS: we would like the designer to find an opportunity for using a photo reflecting this cooperation between therapist, child, teenager and horse. It is a bit up to the designer to find a way to do this... Since the horse is only a tool, among many other tools, it does not have to be much - but we want to try and see how it will work with a photo that also reflects this part of our business.

```html
<!DOCTYPE html>
<html lang="no">
<head>
<meta charset="utf-8">
<title>Fjordlys og Samhold</title>
<link href="https://fonts.googleapis.com/css2?family=Open+Sans:wght@400;600;700&family=Montserrat:wght@400;500;600&display=swap" rel="stylesheet">
<style>
:root{
  --navy:#1d5f8a;
  --brand:#24307a;
  --green:#1f9a3a;
  --sky:#14a0dc;
  --sky-soft:#c5e9fb;
  --sky-faint:#dcebf4;
  --page:#f7f7f7;
  --card:#ececec;
  --ink:#1a1a1a;
  --muted:#555;
  --btn-a:#3fb6e8;
  --btn-b:#1f8fd0;
}
*{box-sizing:border-box;margin:0;padding:0}
html,body{width:1200px;height:3160px;overflow:hidden}
body{position:relative;background:var(--page);font-family:'Montserrat',sans-serif;color:var(--ink)}
.abs{position:absolute}
.heading{font-family:'Open Sans',sans-serif;font-weight:700;color:var(--navy);letter-spacing:1px}

/* nav */
.site-nav{position:absolute;left:0;top:0;width:1200px;height:135px;background:var(--page)}
.nav-link{position:absolute;top:78px;font-size:12px;font-weight:600;color:var(--navy);transform:translateX(-50%)}
.nav-link.active{color:var(--sky)}
.nav-underline{position:absolute;left:240px;top:131px;width:75px;height:3px;background:var(--sky)}
.brand{position:absolute;display:flex;align-items:center;gap:8px;font-family:'Open Sans',sans-serif;font-weight:600;color:var(--brand)}
.brand-dot{width:14px;height:14px;border-radius:50%;background:var(--brand)}

/* hero */
.hero{position:absolute;left:0;top:135px;width:1200px;height:620px}
.hero-title{position:absolute;left:202px;top:244px;font-size:32px}
.hero-sub{position:absolute;left:204px;top:294px;font-family:'Open Sans',sans-serif;font-weight:700;font-size:22px;color:var(--green);letter-spacing:.5px}
.btn{position:absolute;display:flex;align-items:center;justify-content:center;border-radius:40px;background:linear-gradient(90deg,var(--btn-a),var(--btn-b));color:#fff;font-family:'Open Sans',sans-serif;font-weight:700}
.hero-btn{left:201px;top:382px;width:188px;height:58px;font-size:12px}

/* services */
.section-title{position:absolute;font-size:31px}
.service-card{position:absolute;width:368px;height:301px;border-radius:49px;background:var(--card);text-align:center}
.service-icon{position:absolute;left:126px;top:8px;width:117px;height:117px;border-radius:50%;background:#c9c9c9}
.service-name{position:absolute;left:0;width:100%;top:150px;font-family:'Open Sans',sans-serif;font-weight:600;font-size:15px;letter-spacing:1px;color:#111}
.service-text{position:absolute;left:30px;width:308px;top:200px;font-family:'Open Sans',sans-serif;font-size:11px;line-height:21px;color:#333}

/* testimonials */
.testimonials{position:absolute;left:0;top:1666px;width:1200px;height:432px;background:var(--page)}
.leaf-deco{position:absolute;background:radial-gradient(ellipse at center,var(--sky-faint) 0%,rgba(220,235,244,.5) 55%,rgba(247,247,247,0) 75%)}
.avatar{position:absolute;width:76px;height:76px;border-radius:50%;background:linear-gradient(160deg,#8a8a8a,#3a3a3a);transform:translate(-50%,-50%)}
.quote-mark{position:absolute;font-family:'Open Sans',sans-serif;font-weight:700;font-size:150px;line-height:1;color:var(--sky-faint)}
.quote-text{position:absolute;left:555px;width:440px;top:1908px;text-align:center;font-size:11px;line-height:21px;color:#222}
.quote-author{position:absolute;right:207px;top:2068px;font-size:12px;font-weight:500}

/* aktuelt */
.news-band{position:absolute;left:0;top:2126px;width:1200px;height:484px;background:var(--sky-soft)}
.news-card{position:absolute;top:2209px;width:248px;height:298px;border-radius:10px;background:#ececec}
.news-img{position:absolute;left:8px;top:6px;width:232px;height:137px;background:linear-gradient(180deg,#d9dcd8 0%,#b9bfb5 45%,#4f6a3a 75%,#2f4a25 100%)}
.news-title{position:absolute;left:9px;top:149px;font-family:'Open Sans',sans-serif;font-weight:600;font-size:12px;letter-spacing:.5px;color:#111}
.news-meta{position:absolute;left:9px;top:172px;font-size:10px;font-weight:500;color:#222}
.news-text{position:absolute;left:9px;top:194px;width:232px;font-size:8.5px;line-height:21px;color:#555;text-transform:uppercase}
.dot{position:absolute;top:2536px;width:12px;height:12px;border-radius:50%;background:#fff}

/* cta */
.cta-title{position:absolute;left:720px;top:2666px;font-family:'Open Sans',sans-serif;font-weight:600;font-size:33px;letter-spacing:4px;color:#fff}
.cta-title span{color:var(--sky)}
.cta-sub{position:absolute;left:722px;top:2707px;font-size:11px;color:#fff}

/* footer */
.foot-head{position:absolute;font-size:11.5px;font-weight:500;color:#222}
.foot-link{position:absolute;font-size:9.5px;color:#555}
.social{position:absolute;top:2937px;width:18px;height:18px;border-radius:50%;background:#222}
.foot-line{position:absolute;left:151px;top:3102px;width:899px;height:2px;background:#8cc8ec}
.foot-small{position:absolute;top:3126px;font-size:10px;color:#333}
</style>
</head>
<body>

<header class="site-nav">
  <span class="nav-link active" style="left:278px">HJEM</span>
  <span class="nav-link" style="left:408px">TJENESTER</span>
  <div class="brand" style="left:507px;top:72px;font-size:17px"><span class="brand-dot"></span>Fjordlys og Samhold</div>
  <span class="nav-link" style="left:770px">AKTUELT</span>
  <span class="nav-link" style="left:908px">KONTAKT</span>
  <div class="nav-underline"></div>
</header>

<svg class="hero" viewBox="0 0 1200 620" role="img" aria-label="Photo: young man in a blue sweater standing on a rock, looking over misty mountains at sunrise">
  <defs>
    <linearGradient id="heroSky" x1="0" y1="0" x2="0" y2="1">
      <stop offset="0" stop-color="#f3d7b0"/>
      <stop offset=".3" stop-color="#e7c7a2"/>
      <stop offset=".5" stop-color="#9a9aa2"/>
      <stop offset=".75" stop-color="#5d6670"/>
      <stop offset="1" stop-color="#3f4a52"/>
    </linearGradient>
  </defs>
  <rect width="1200" height="620" fill="url(#heroSky)"/>
  <path d="M0 599 C 120 585, 180 570, 245 570 C 420 570, 700 610, 900 617 C 1050 622, 1150 618, 1200 618 L1200 620 L0 620 Z" fill="#f7f7f7"/>
</svg>
<h1 class="heading hero-title">NÅ DITT SANNE POTENSIALE</h1>
<p class="hero-sub">KJENN KRAFTEN DIN NÅ</p>
<a class="btn hero-btn">KOM I GANG</a>

<h2 class="heading section-title" style="left:202px;top:800px">VÅRE TJENESTER</h2>

<article class="service-card" style="left:160px;top:914px">
  <div class="service-icon" role="img" aria-label="Illustration: clipboard with medical cross"></div>
  <h3 class="service-name">UTREDNING</h3>
  <p class="service-text">Lorem ipsum dolor sit amet, consectetur adipisicing elit, sed do eiusmod tempor incididunt ut labore et dolore magna aliqua.</p>
</article>
<article class="service-card" style="left:673px;top:914px">
  <div class="service-icon" role="img" aria-label="Illustration: consultant on a screen with speech bubble"></div>
  <h3 class="service-name">RÅDGIVNING</h3>
  <p class="service-text">Ut enim ad minim veniam, quis nostrud exercitation ullamco laboris nisi ut aliquip ex ea commodo consequat.</p>
</article>
<article class="service-card" style="left:160px;top:1291px">
  <div class="service-icon" role="img" aria-label="Illustration: browser window with video player"></div>
  <h3 class="service-name">KURS OG WORK SHOPS</h3>
  <p class="service-text">Duis aute irure dolor in reprehenderit in voluptate velit esse cillum dolore eu fugiat nulla pariatur.</p>
</article>
<article class="service-card" style="left:673px;top:1291px">
  <div class="service-icon" role="img" aria-label="Illustration: open hand holding green leaves"></div>
  <h3 class="service-name">TERAPI OG UTVIKLING</h3>
  <p class="service-text">Sed ut perspiciatis unde omnis iste natus error sit voluptatem accusantium doloremque laudantium, totam rem aperiam, eaque ipsa quae ab illo inventore veritatis et quasi architecto beatae explicabo.</p>
</article>

<section class="testimonials">
  <div class="leaf-deco" role="img" aria-label="Faint leaf decoration" style="left:-40px;top:90px;width:300px;height:300px"></div>
  <div class="leaf-deco" role="img" aria-label="Faint leaf decoration" style="left:1030px;top:-20px;width:200px;height:220px"></div>
</section>
<h2 class="heading section-title" style="left:200px;top:1731px">HVA FOLK SIER?</h2>
<div class="quote-mark" style="left:490px;top:1725px">“</div>
<div class="quote-mark" style="left:960px;top:1960px">”</div>
<svg class="abs" style="left:155px;top:1888px" width="16" height="24" viewBox="0 0 16 24"><path d="M13 2 L3 12 L13 22" fill="none" stroke="var(--navy)" stroke-width="2"/></svg>
<svg class="abs" style="left:1030px;top:1888px" width="16" height="24" viewBox="0 0 16 24"><path d="M3 2 L13 12 L3 22" fill="none" stroke="var(--navy)" stroke-width="2"/></svg>
<div class="avatar" role="img" aria-label="Portrait photo of a client" style="left:335px;top:1847px"></div>
<div class="avatar" role="img" aria-label="Portrait photo of a client" style="left:433px;top:1847px"></div>
<div class="avatar" role="img" aria-label="Portrait photo of a client" style="left:228px;top:1945px"></div>
<div class="avatar" role="img" aria-label="Portrait photo of a client" style="left:333px;top:1945px"></div>
<div class="avatar" role="img" aria-label="Portrait photo of a client" style="left:437px;top:1945px"></div>
<div class="avatar" role="img" aria-label="Portrait photo of a client" style="left:228px;top:2043px"></div>
<div class="avatar" role="img" aria-label="Portrait photo of a client" style="left:342px;top:2043px"></div>
<p class="quote-text">Nemo enim ipsam voluptatem quia voluptas sit aspernatur aut odit aut fugit, sed quia consequuntur magni dolores eos qui ratione voluptatem sequi nesciunt. Neque porro quisquam est, qui dolorem ipsum quia dolor sit amet, consectetur, adipisci velit.</p>
<p class="quote-author">- Henrik Dahl (24 years old)</p>

<div class="news-band"></div>
<svg class="abs" style="left:0;top:2098px" width="677" height="78" viewBox="0 0 677 78"><path d="M0 0 H677 L640 39 L677 78 H0 Z" fill="var(--sky)"/></svg>
<h2 class="heading section-title" style="left:201px;top:2116px;color:#fff">AKTUELT</h2>

<article class="news-card" style="left:157px">
  <div class="news-img" role="img" aria-label="Photo: football on a grass field with a tree"></div>
  <h3 class="news-title">NEMO ENIM IPSAM VOLUPTATEM</h3>
  <p class="news-meta">04 FEB 20 &nbsp; 7 MINUTE READ</p>
  <p class="news-text">Duis aute irure dolor in reprehenderit in voluptate velit esse cillum dolore eu fugiat nulla pariatur. Excepteur...</p>
</article>
<article class="news-card" style="left:476px">
  <div class="news-img" role="img" aria-label="Photo: football on a grass field with a tree"></div>
  <h3 class="news-title">NEMO ENIM IPSAM VOLUPTATEM</h3>
  <p class="news-meta">04 FEB 20 &nbsp; 7 MINUTE READ</p>
  <p class="news-text">Duis aute irure dolor in reprehenderit in voluptate velit esse cillum dolore eu fugiat nulla pariatur. Excepteur...</p>
</article>
<article class="news-card" style="left:795px">
  <div class="news-img" role="img" aria-label="Photo: football on a grass field with a tree"></div>
  <h3 class="news-title">NEMO ENIM IPSAM VOLUPTATEM</h3>
  <p class="news-meta">04 FEB 20 &nbsp; 7 MINUTE READ</p>
  <p class="news-text">Duis aute irure dolor in reprehenderit in voluptate velit esse cillum dolore eu fugiat nulla pariatur. Excepteur...</p>
</article>
<span class="dot" style="left:557px;background:var(--sky)"></span>
<span class="dot" style="left:582px"></span>
<span class="dot" style="left:605px"></span>
<span class="dot" style="left:630px"></span>

<svg class="abs" style="left:0;top:2610px" width="1200" height="249" viewBox="0 0 1200 249" role="img" aria-label="Photo: hiker in a red jacket facing snowy mountains">
  <defs>
    <linearGradient id="ctaBg" x1="0" y1="0" x2="1" y2="0">
      <stop offset="0" stop-color="#8fa0b0"/>
      <stop offset=".4" stop-color="#c9d3dc"/>
      <stop offset=".7" stop-color="#7d8791"/>
      <stop offset="1" stop-color="#5a6068"/>
    </linearGradient>
  </defs>
  <rect width="1200" height="249" fill="url(#ctaBg)"/>
  <circle cx="932" cy="126" r="245" fill="#2e3238" fill-opacity=".55"/>
</svg>
<h2 class="cta-title">START <span>REISEN</span> NÅ</h2>
<p class="cta-sub">KJENNE DINE MÅL OG NÅ DITT VIRKELIGE POTENSIAL</p>
<a class="btn" style="left:810px;top:2752px;width:134px;height:36px;font-size:8px">KOM I GANG</a>

<footer>
  <div class="brand" style="left:160px;top:2970px;font-size:18px"><span class="brand-dot"></span>Fjordlys og Samhold</div>

  <h4 class="foot-head" style="left:424px;top:2911px">RASK LINK</h4>
  <span class="foot-link" style="left:424px;top:2934px">HJEM</span>
  <span class="foot-link" style="left:424px;top:2955px">OM OSS</span>
  <span class="foot-link" style="left:424px;top:2976px">TERAPI</span>
  <span class="foot-link" style="left:424px;top:2997px">FORDELER</span>
  <span class="foot-link" style="left:424px;top:3018px">BLOG</span>

  <h4 class="foot-head" style="left:594px;top:2911px">KONTAKT OSS</h4>
  <svg class="abs" style="left:594px;top:2935px" width="18" height="18" viewBox="0 0 18 18"><path d="M9 1 C5.5 1 3.5 3.5 3.5 6.5 C3.5 10 9 15 9 15 C9 15 14.5 10 14.5 6.5 C14.5 3.5 12.5 1 9 1 Z" fill="var(--navy)"/><circle cx="9" cy="6.5" r="2" fill="#fff"/><path d="M2 17 H16" stroke="#333" stroke-width="1.2"/></svg>
  <span class="foot-link" style="left:623px;top:2939px;width:215px;line-height:21px">12 BRYGGEGATA, FJORDVIK,<br>NORGE</span>
  <svg class="abs" style="left:594px;top:2987px" width="18" height="13" viewBox="0 0 18 13"><rect x="1" y="1" width="16" height="11" fill="none" stroke="#333" stroke-width="1.3"/><path d="M1 1 L9 7 L17 1" fill="none" stroke="#333" stroke-width="1.3"/></svg>
  <span class="foot-link" style="left:623px;top:2987px">POST@FJORDLYS-SAMHOLD.NO</span>
  <svg class="abs" style="left:597px;top:3014px" width="12" height="18" viewBox="0 0 12 18"><rect x="1" y="1" width="10" height="16" rx="1.5" fill="none" stroke="#333" stroke-width="1.5"/><circle cx="6" cy="14" r="1" fill="#333"/></svg>
  <span class="foot-link" style="left:623px;top:3018px">+47 412-3456-789</span>

  <h4 class="foot-head" style="left:864px;top:2911px">HOLD KONTAKTEN</h4>
  <span class="social" style="left:865px"></span>
  <span class="social" style="left:890px"></span>
  <span class="social" style="left:915px"></span>
  <span class="social" style="left:941px"></span>
  <span class="social" style="left:966px"></span>

  <div class="foot-line"></div>
  <span class="foot-small" style="left:152px">©2020 FJORDLYS OG SAMHOLD ALL RIGHTS RESERVED</span>
  <span class="foot-small" style="left:767px">PERSONVERN</span>
  <span class="foot-small" style="left:877px">|</span>
  <span class="foot-small" style="left:915px">VILKÅR OG BETINGELSER</span>
</footer>

</body>
</html>
```